Quiet Harbor Podcast Business Card Design

Needing a business card with the logo design provided for Quiet Harbor Podcast. I am looking for a modern style that fits the current logo.

Info:
Name: Teodor Vask
Title: Creator/Host
Email: teodor@quietharborcast.com
Phone: (555) 274-9163
www.quietharborcast.com
Twitter: @qharborcast
Instagram: @quietharborcastshow
Facebook: Quiet Harbor Podcast

Industry/Entity Type

Business

Font styles to use
Sans Serif

Colors
000000
ffffff

Requirements
Must have
• modern, clean design
Nice to have
• social media contact info

```html
<!DOCTYPE html>
<html lang="en">
<head>
<meta charset="utf-8">
<title>Quiet Harbor Podcast — Business Card</title>
<link href="https://fonts.googleapis.com/css2?family=Lato:wght@400;700;900&display=swap" rel="stylesheet">
<style>
  :root {
    --backdrop: #e9e6e1;
    --card-light: #ffffff;
    --card-dark: #212121;
    --ink: #1b1b1b;
    --ink-soft: #4a4a4a;
    --paper: #ffffff;
    --rule: #8a8a8a;
  }
  * { margin: 0; padding: 0; box-sizing: border-box; }
  html, body { width: 1200px; height: 1000px; overflow: hidden; }
  body { background: var(--backdrop); font-family: "Lato", Arial, sans-serif; }
  .stage { position: relative; width: 1200px; height: 1000px; }

  .card {
    position: absolute; left: 240px; width: 696px; height: 396px;
    border-radius: 22px;
    box-shadow: 0 6px 14px rgba(0,0,0,.25);
  }
  .card--front { top: 82px; background: var(--card-light); }
  .card--back { top: 520px; background: var(--card-dark); }

  /* front: brand block */
  .brand { position: absolute; text-align: center; color: var(--ink); }
  .brand--front { left: 40px; top: 132px; width: 276px; }
  .brand__square { display: block; margin: 0 auto 14px; width: 58px; height: 58px; background: currentColor; }
  .brand__name { font-weight: 900; font-size: 26px; line-height: 1; letter-spacing: 0; }
  .brand__sub { font-weight: 900; font-size: 11px; letter-spacing: 5px; margin-top: 6px; padding-left: 5px; }

  .divider {
    position: absolute; left: 334px; top: 100px; width: 2px; height: 198px;
    background: linear-gradient(to bottom, rgba(0,0,0,0), var(--rule) 20%, var(--rule) 80%, rgba(0,0,0,0));
  }

  .contact { position: absolute; left: 363px; top: 100px; color: var(--ink-soft); }
  .contact__name { font-size: 21px; color: var(--ink); letter-spacing: .5px; line-height: 24px; }
  .contact__title { font-size: 15px; color: var(--ink); line-height: 20px; }
  .contact__list { list-style: none; margin-top: 13px; }
  .contact__list + .contact__list { margin-top: 12px; }
  .contact__item { display: flex; align-items: center; height: 21px; font-size: 15.5px; }
  .contact__icon { width: 13px; height: 13px; margin-right: 18px; flex: none; fill: var(--ink); }
  .contact__badge { width: 12px; height: 12px; margin-right: 19px; flex: none; background: var(--ink); border-radius: 2px; }

  /* back */
  .brand--back { left: 0; width: 696px; top: 95px; color: var(--paper); }
  .brand--back .brand__square { width: 112px; height: 112px; margin-bottom: 40px; }
  .brand--back .brand__name { font-size: 41px; }
  .brand--back .brand__sub { font-size: 17px; letter-spacing: 8px; padding-left: 8px; margin-top: 10px; }
</style>
</head>
<body>
<main class="stage">
  <section class="card card--front" aria-label="Card front">
    <div class="brand brand--front">
      <span class="brand__square"></span>
      <div class="brand__name">QUIET HARBOR</div>
      <div class="brand__sub">PODCAST</div>
    </div>
    <div class="divider"></div>
    <div class="contact">
      <div class="contact__name">TEODOR VASK</div>
      <div class="contact__title">Creator/Host</div>
      <ul class="contact__list">
        <li class="contact__item">
          <svg class="contact__icon" viewBox="0 0 16 16"><path d="M3.5 1.5l2.5 0 1.2 3.2-1.6 1.2c.8 1.8 2.2 3.2 4 4l1.2-1.6 3.2 1.2v2.5c0 .8-.7 1.5-1.5 1.5C6.6 13.5 2 8.9 2 3c0-.8.7-1.5 1.5-1.5z"/></svg>
          (555) 274-9163
        </li>
        <li class="contact__item">
          <svg class="contact__icon" viewBox="0 0 16 16"><path d="M1 3h14v1.2L8 8.6 1 4.2z"/><path d="M1 5.8l7 4.4 7-4.4V13H1z"/></svg>
          teodor@quietharborcast.com
        </li>
        <li class="contact__item">
          <svg class="contact__icon" viewBox="0 0 16 16"><circle cx="8" cy="8" r="6.5" fill="none" stroke="#1b1b1b" stroke-width="1.6"/><path d="M1.5 8h13M8 1.5c-3 3.5-3 9.5 0 13M8 1.5c3 3.5 3 9.5 0 13" fill="none" stroke="#1b1b1b" stroke-width="1.2"/></svg>
          www.quietharborcast.com
        </li>
      </ul>
      <ul class="contact__list">
        <li class="contact__item"><span class="contact__badge"></span>Quiet Harbor Podcast</li>
        <li class="contact__item"><span class="contact__badge"></span>@qharborcast</li>
        <li class="contact__item"><span class="contact__badge"></span>@quietharborcastshow</li>
      </ul>
    </div>
  </section>

  <section class="card card--back" aria-label="Card back">
    <div class="brand brand--back">
      <span class="brand__square"></span>
      <div class="brand__name">QUIET HARBOR</div>
      <div class="brand__sub">PODCAST</div>
    </div>
  </section>
</main>
</body>
</html>
```